Nursing Student Card: Chipped Pastels Still Shine

Side 1:
Business card 2.5" x 2.5" size
Phrase: Chipped Pastels Still Shine
Target market: Nursing Students studying Pediatrics
The attached picture is too basic. I am looking for something with compassion, beauty and graceful movement. Color and font is at your discretion. Will probably chose a pearlescent card stock for printing.

Side 2:
Courtesy of Dr. Lorinda Beckwith RN PhD

Target Market(s)

Mostly female nursing students between ages 23-35.

```html
<!DOCTYPE html>
<html lang="en">
<head>
<meta charset="UTF-8">
<title>Chipped Pastels Still Shine – Card</title>
<link rel="stylesheet" href="https://fonts.googleapis.com/css2?family=Poppins:wght@400;500;700&display=swap">
<style>
  :root {
    --page-bg: #ece8e3;
    --ink-black: #1a1a1a;
    --panel: #e8f5fd;
    --panel-edge: #e8641c;
    --courtesy: #2b3f9e;
  }
  * { margin: 0; padding: 0; box-sizing: border-box; }
  html, body { width: 1200px; height: 800px; overflow: hidden; }
  body {
    background: var(--page-bg);
    display: flex;
    align-items: center;
    justify-content: center;
    gap: 80px;
  }
  .card {
    position: relative;
    width: 460px;
    height: 460px;
    border-radius: 22px;
    overflow: hidden;
    box-shadow: 0 10px 28px rgba(0,0,0,0.18);
  }
  .crayon-field {
    position: absolute;
    inset: 0;
    background:
      radial-gradient(circle at 20% 25%, rgba(245,201,21,0.85), transparent 30%),
      radial-gradient(circle at 75% 20%, rgba(45,154,60,0.8), transparent 32%),
      radial-gradient(circle at 30% 80%, rgba(211,38,43,0.8), transparent 32%),
      radial-gradient(circle at 80% 75%, rgba(44,86,184,0.85), transparent 30%),
      radial-gradient(circle at 55% 50%, rgba(232,85,160,0.7), transparent 30%),
      linear-gradient(135deg, #f08a1c, #2a8fd0 50%, #3a9e46);
  }
  .title {
    position: absolute;
    left: 34px;
    top: 44px;
    font-family: "Poppins", "Helvetica", sans-serif;
    font-weight: 700;
    font-size: 58px;
    line-height: 1.08;
    letter-spacing: 1px;
    color: var(--ink-black);
  }
  .title .line { display: block; }
  .title .line-1 { padding-left: 88px; }
  .title .line-2 { padding-left: 30px; }
  .title .line-3 { padding-left: 14px; }

  .back-panel {
    position: absolute;
    inset: 34px;
    background: var(--panel);
    border: 2px solid var(--panel-edge);
    border-radius: 16px;
    display: flex;
    flex-direction: column;
    align-items: center;
    justify-content: center;
    font-family: "Poppins", "Helvetica", sans-serif;
    text-align: center;
  }
  .courtesy { color: var(--courtesy); font-size: 17px; font-weight: 400; }
  .sponsor { color: var(--ink-black); font-size: 18px; font-weight: 500; margin-top: 2px; }
</style>
</head>
<body>
  <section class="card card-front">
    <div class="crayon-field" role="img" aria-label="Photo of many broken multicoloured crayon pieces"></div>
    <h1 class="title">
      <span class="line line-1">CHIPPED</span>
      <span class="line line-2">PASTELS</span>
      <span class="line line-3">STILL</span>
      <span class="line line-4">SHINE</span>
    </h1>
  </section>

  <section class="card card-back">
    <div class="crayon-field" role="img" aria-label="Photo border of broken multicoloured crayon pieces"></div>
    <div class="back-panel">
      <p class="courtesy">Courtesy of</p>
      <p class="sponsor">Dr. Lorinda Beckwith RN PhD</p>
    </div>
  </section>
</body>
</html>
```